COMMERCIAL REAL ESTATE FLYER TEMPLATE

We need a template flyer designed that we can use for a current commercial real estate listing and subsequently use as a template for future listings. We have uploaded images and files to provide an example of an older flyer template we have used. If you have questions or would like to discuss, please contact us at Wade@TLMVX.net. Colors selected should be in line with our attached business card and logo design. Output should be 8.5" X 11".

Target Market(s)

Commercial Real Estate. NO RESIDENTIAL. Needs to have a professional commercial presentation with no reference to residential real estate.

Industry/Entity Type

Real Estate Agent

Font styles to use
Serif

Colors

Designer to choose colors to be used in the design.

Requirements
Must have
• MUST BE SAVED AND ADJUSTABLE IN ONE OF THE FOLLOWING FORMATES: MICROSOFT POWERPOINT, PUBLISHER OR WORD. THIS IS IMPORTANT SO OUR TEAM CAN EASILLY UPDATE TEMPLATE IN READILLY AVAILABLE PROGRAMS THAT ARE SIMPLE FOR TEAM MEMBERS TO USE.
Nice to have
• Needs to have first page template with header and footer displaying our logo, address, phone, email address and contact information for the listing agent. There need to be placeholders that can be easily adjusted based on specific listings. Placeholders will be used for pictures or aerials as the case requires. Needs to have a second page that has header and footer with a clean open block in the middle of the page so agents can customize with site specific details.
Should not have
• There should be no reference to residential. We are a commercial real estate organization that does not do any residential.

```html
<!DOCTYPE html>
<html lang="en">
<head>
<meta charset="utf-8">
<title>Tallmon Commercial Real Estate – Listing Flyer</title>
<link href="https://fonts.googleapis.com/css2?family=Oswald:wght@300;400;500&display=swap" rel="stylesheet">
<style>
  :root {
    --brand-red: #b8232f;
    --brand-navy: #1f2944;
    --paper: #ffffff;
    --panel-top: #ffffff;
    --panel-bottom: #dedfe1;
    --ink: #1c1c1c;
    --stage: #e9e8e6;
    --fine-print: #d9dce4;
  }
  * { box-sizing: border-box; margin: 0; padding: 0; }
  html, body { width: 1200px; height: 1200px; overflow: hidden; }
  body { background: var(--stage); font-family: "Oswald", sans-serif; position: relative; }

  .flyer {
    position: absolute; left: 220px; top: 108px;
    width: 760px; height: 984px;
    background: var(--paper);
    box-shadow: 0 6px 24px rgba(0,0,0,.18);
    overflow: hidden;
  }
  .photo { position: absolute; display: block; }
  .photo-hero { left: 0; top: 0; width: 760px; height: 380px;
    background: linear-gradient(160deg, #dcdccf 0%, #b9b59c 45%, #8a6a4a 70%, #a59c8d 100%); }
  .photo-kitchen { left: 300px; top: 396px; width: 460px; height: 294px;
    background: linear-gradient(170deg, #d9d6c2 0%, #b88c52 45%, #c8bba2 75%, #ddd3bf 100%); }
  .photo-workstation { left: 350px; top: 702px; width: 182px; height: 158px;
    background: linear-gradient(170deg, #cfcab2 0%, #b7ad94 60%, #d6cfbd 100%); }
  .photo-lounge { left: 542px; top: 702px; width: 218px; height: 158px;
    background: linear-gradient(165deg, #d5d1c0 0%, #a98a62 50%, #d2c6b6 100%); }

  .brand-block {
    position: absolute; left: 0; top: 110px; width: 150px; height: 190px;
    background: var(--brand-red); color: #fff;
    display: flex; flex-direction: column; justify-content: flex-end;
    padding: 0 14px 22px;
  }
  .brand-name { display: flex; align-items: center; gap: 6px; font-size: 15px; font-weight: 500; letter-spacing: .5px; line-height: 1; }
  .brand-square { width: 10px; height: 10px; background: #fff; flex: none; }
  .brand-tag { font-size: 11px; font-weight: 400; letter-spacing: .3px; margin-top: 3px; }

  .listings-panel {
    position: absolute; left: 0; top: 380px; width: 300px; height: 410px;
    background: linear-gradient(180deg, var(--panel-top) 0%, var(--panel-bottom) 100%);
    padding: 40px 16px 0 28px; color: var(--ink);
  }
  .listings-title { font-size: 30px; font-weight: 400; letter-spacing: .5px; margin-bottom: 14px; }
  .listings-title .accent { color: var(--brand-red); }
  .listings-list { list-style: none; font-size: 16.5px; font-weight: 300; line-height: 1.6; }
  .listings-terms { margin-top: 18px; font-size: 16.5px; font-weight: 400; }

  .agent-block {
    position: absolute; left: 0; top: 790px; width: 340px; height: 194px;
    background: var(--brand-red); color: #fff;
    padding: 30px 28px; font-size: 19px; font-weight: 400; line-height: 1.45;
  }
  .agent-name { font-weight: 500; }

  .disclaimer {
    position: absolute; left: 340px; top: 868px; width: 420px; height: 116px;
    background: var(--brand-navy); color: var(--fine-print);
    padding: 8px 12px; font-size: 10px; font-weight: 300; line-height: 1.38;
  }
</style>
</head>
<body>
  <main class="flyer">
    <div class="photo photo-hero" role="img" aria-label="Private office with wooden desk, hutch and guest seating"></div>

    <div class="brand-block">
      <div class="brand-name"><span class="brand-square"></span>TALLMON</div>
      <div class="brand-tag">COMMERCIAL REAL ESTATE</div>
    </div>

    <section class="listings-panel">
      <h1 class="listings-title"><span class="accent">CURRENT</span> LISTINGS</h1>
      <ul class="listings-list">
        <li>Well Maintained Owner-Occupied Building</li>
        <li>Great Location Near Route 9 &amp; Cedar Hollow</li>
        <li>Easy Access To Route 9 &amp; Loop 12</li>
        <li>Building Size: 6,400 SF (CCAD)</li>
        <li>Land Area: 0.85 Acres (CCAD)</li>
        <li>Office Space: 2,820 SF (Owner)</li>
        <li>Loading: Grade-Level Doors</li>
        <li>Eave Height: 22'</li>
        <li>Outside Storage: Room To Add Fenced Yard</li>
      </ul>
      <p class="listings-terms">TERMS: CONTACT BELOW</p>
    </section>

    <div class="photo photo-kitchen" role="img" aria-label="Break room with wooden cabinets, refrigerator and dining table"></div>
    <div class="photo photo-workstation" role="img" aria-label="Open workroom with computer station"></div>
    <div class="photo photo-lounge" role="img" aria-label="Office lounge with desk, bookshelf and armchair"></div>

    <section class="agent-block">
      <p class="agent-name">Wade Tallmon</p>
      <p>Broker / CEO</p>
      <p>(555) 014-2286</p>
      <p>Wade@TLMVX.net</p>
      <p>Broker License:</p>
    </section>

    <footer class="disclaimer">
      The information contained herein has, we believe, been obtained from reliable sources, and we have no reason to doubt the accuracy thereof. All such information is submitted subject to errors, omissions or changes in condition prior to sale, lease or withdrawal without notice. All information contained herein should be verified by the person relying thereon. We have not made and will not make any warranty or representation as to the condition of the property nor the presence of any hazardous substances or any environmental or other conditions that may affect the value or suitability of the property.
    </footer>
  </main>
</body>
</html>
```